Willow Ember Uniform Label Redesign

To refine our current product label designs into one, simple, modern, crisp, general look that can be adapted to all our all Natural Skin Care and Wellness products. I am inspired by the elegant versatility of products like Corvalis Botanic Beauty or Tidal Beauty label schemes. We no longer want labels that indicate scent or ingredients. We have two primary colors that we want to maintain (#096CA3 and #DEE33F), and are willing to entertain subtle additions of others, other than black. Our labels will be printed on white or clear material. We use mainly Cosmo or Boston Round container shapes, plus flat top, smooth, round jars. Maybe a faded watermark highlight the "natural" or "beautiful" side of our products. we need to convey confidence, while remaining simple. We currently use the Advantage font. Maybe Century Gothic may work. Something similar that is easy on the eyes. Maybe vertical main text? We are willing to entertain a lot of ideas. These designs will offer ideas into our eventual Website (www.willowember.com) redesign.

Target Market(s)

Those who are familiar with the power of natural, plant based skin care and wellness products

Industry/Entity Type

Natural Skin Care and Wellness

Font styles to use
Sans Serif
Other font styles liked:
• Century Gothic, Advantage, or similar that is easy on the eyes

Colors
0054AA
0677BA
7BADD7
CADEEF
E8F1F8
59FF00
82FF00
B8FF75
E3FFCB
F4FFEA

Requirements
Must have
• "Clean Lines"; These colors: (#096CA3 and #DEE33F)
Nice to have
• MAYBE vertical main text or a watermark image

```html
<!DOCTYPE html>
<html lang="en">
<head>
<meta charset="utf-8">
<title>Willow Ember – Hydrating Lotion Labels</title>
<link rel="stylesheet" href="https://fonts.googleapis.com/css2?family=Questrial&family=Yanone+Kaffeesatz:wght@300&display=swap">
<style>
  :root {
    --paper: #ffffff;
    --lime-light: #e3e683;
    --lime: #dee33f;
    --lime-deep: #b3b61b;
    --ocean: #096ca3;
    --ocean-deep: #1b447a;
    --ocean-soft: #46709a;
    --sky-text: #4f8fc4;
    --ink: #3c3c3c;
  }
  html, body {
    margin: 0;
    width: 1200px;
    height: 987px;
    overflow: hidden;
    background: var(--paper);
  }
  .sheet {
    position: relative;
    width: 1200px;
    height: 987px;
  }
  .label {
    position: absolute;
    top: 311px;
    width: 200px;
    height: 560px;
    font-family: "Questrial", "Century Gothic", sans-serif;
  }
  .label--one   { left: 143px; }
  .label--two   { left: 497px; }
  .label--three { left: 850px; }

  .brand-panel {
    position: absolute;
    left: 0; top: 0;
    width: 128px; height: 490px;
    background: linear-gradient(90deg, var(--lime-light) 0%, var(--lime) 45%, var(--lime-deep) 100%);
  }
  .vertical {
    position: absolute;
    writing-mode: vertical-rl;
    transform: rotate(180deg);
    white-space: nowrap;
  }
  .wordmark {
    left: 18px; top: 30px;
    height: 343px;
    font-family: "Yanone Kaffeesatz", "Questrial", sans-serif;
    font-weight: 300;
    font-size: 66px;
    line-height: 66px;
    text-align: left;
    color: var(--sky-text);
  }
  .wordmark--light { color: var(--paper); }
  .brand-dot {
    position: absolute;
    left: 17px; top: 390px;
    width: 90px; height: 90px;
    border-radius: 50%;
    background: var(--paper);
  }
  .tagline {
    left: 104px; top: 50px;
    height: 350px;
    font-size: 14px;
    line-height: 18px;
    letter-spacing: 0.16em;
    text-align: left;
    color: var(--ocean);
  }
  .tagline--dark { color: var(--ocean-deep); }
  .tagline .dot { padding: 4px 0; }

  .product-band {
    position: absolute;
    top: 0; height: 490px;
  }
  .product-band--rule-after { left: 128px; width: 62px; }
  .product-band--rule-after::after {
    content: "";
    position: absolute;
    right: 0; top: 0;
    width: 7px; height: 487px;
    background: var(--ocean-deep);
  }
  .product-band--filled {
    left: 128px; width: 62px;
    background: linear-gradient(90deg, var(--ocean-deep) 0%, var(--ocean-deep) 40%, var(--ocean-soft) 100%);
  }
  .product-band--rule-before { left: 128px; width: 62px; }
  .product-band--rule-before::before {
    content: "";
    position: absolute;
    left: 0; top: 0;
    width: 7px; height: 490px;
    background: var(--ocean-deep);
  }
  .product-name {
    top: 22px;
    height: 440px;
    font-size: 23px;
    line-height: 28px;
    letter-spacing: 0.42em;
    text-align: left;
    color: var(--ocean-deep);
  }
  .product-band--rule-after .product-name  { left: 22px; }
  .product-band--filled .product-name      { left: 22px; color: var(--paper); }
  .product-band--rule-before .product-name { left: 28px; color: var(--ocean-soft); }

  .details {
    position: absolute;
    left: 0; top: 500px;
    width: 200px;
    text-align: center;
    color: var(--ink);
  }
  .details .variant {
    font-size: 22px;
    letter-spacing: 0.02em;
    line-height: 26px;
  }
  .details .volume {
    font-size: 17px;
    line-height: 24px;
    color: #555;
  }
</style>
</head>
<body>
<main class="sheet">

  <section class="label label--one">
    <div class="brand-panel">
      <span class="vertical wordmark">Willow Ember</span>
      <span class="brand-dot"></span>
      <span class="vertical tagline">SIMPLE <span class="dot">•</span> BEAUTIFUL <span class="dot">•</span> TIMELESS</span>
    </div>
    <div class="product-band product-band--rule-after">
      <span class="vertical product-name">HYDRATING LOTION</span>
    </div>
    <div class="details">
      <div class="variant">ALOE AND SHEA</div>
      <div class="volume">8 fl. oz (238ml)</div>
    </div>
  </section>

  <section class="label label--two">
    <div class="brand-panel">
      <span class="vertical wordmark wordmark--light">Willow Ember</span>
      <span class="brand-dot"></span>
      <span class="vertical tagline tagline--dark">SIMPLE <span class="dot">•</span> BEAUTIFUL <span class="dot">•</span> TIMELESS</span>
    </div>
    <div class="product-band product-band--filled">
      <span class="vertical product-name">HYDRATING LOTION</span>
    </div>
    <div class="details">
      <div class="variant">ALOE AND SHEA</div>
      <div class="volume">8 fl. oz (238ml)</div>
    </div>
  </section>

  <section class="label label--three">
    <div class="brand-panel">
      <span class="vertical wordmark wordmark--light">Willow Ember</span>
      <span class="brand-dot"></span>
      <span class="vertical tagline tagline--dark">SIMPLE <span class="dot">•</span> BEAUTIFUL <span class="dot">•</span> TIMELESS</span>
    </div>
    <div class="product-band product-band--rule-before">
      <span class="vertical product-name">HYDRATING LOTION</span>
    </div>
    <div class="details">
      <div class="variant">ALOE AND SHEA</div>
      <div class="volume">8 fl. oz (238ml)</div>
    </div>
  </section>

</main>
</body>
</html>
```